Design a leading edge business card for an architectural company

We believe that Velistra Design Collective is redefining the architectural industry. With that, we need a leading edge business card for the company that focuses on landscape architecture, design, and construction.

Our clients are businesses and homeowners so we need a clean, simple, and professional-looking logo. But we want something special. Design must be elegant but unexpected.

Color preferences:
- Preferably with black background but not a must
- Text should be light colored
- Overall, don’t use too much colors.

Content:
- Front of card must contain either just the logo or the logo and business name only.
- Back of card will show the other information (name, title, phone number, email, website, location).

Style:
- Maybe embossing, de-bossing, or spot UV
- Layout should be landscape unless you prove us otherwise.

Size: 1050 x 600 pixels (with 1/8th inch bleed: 1125 x 675 pixels)

Attached is the company logo to incorporate in the design.

```html
<!DOCTYPE html>
<html lang="en">
<head>
<meta charset="utf-8">
<title>Velistra Design Collective – Business Card</title>
<link href="https://fonts.googleapis.com/css2?family=Cinzel:wght@400&family=Arimo:wght@400&display=swap" rel="stylesheet">
<style>
  :root {
    --page-bg: #e9e7e4;
    --card-top: #5a5a5c;
    --card-mid: #2c2c2e;
    --card-bottom: #121213;
    --ink-light: #f2f2f2;
    --ink-soft: #c9c9cb;
    --bar-light: #ffffff;
    --bar-shade: #cfcfcf;
    --bar-ink: #1a1a1a;
    --shadow: rgba(0,0,0,0.35);
  }
  * { margin: 0; padding: 0; box-sizing: border-box; }
  html, body { width: 1200px; height: 912px; overflow: hidden; }
  body {
    background: var(--page-bg);
    position: relative;
    font-family: "Arimo", Arial, sans-serif;
  }
  .card {
    position: absolute;
    left: 250px;
    width: 700px;
    height: 400px;
    border-radius: 4px;
    background: linear-gradient(160deg, var(--card-top) 0%, var(--card-mid) 45%, var(--card-bottom) 100%);
    box-shadow: 0 10px 24px var(--shadow);
    overflow: hidden;
  }
  .card--front { top: 40px; }
  .card--back { top: 472px; }

  .brand {
    position: absolute;
    left: 0; right: 0;
    text-align: center;
    font-family: "Cinzel", Georgia, serif;
    font-weight: 400;
    color: var(--ink-light);
    letter-spacing: 0.14em;
    text-transform: uppercase;
  }
  .brand__dot {
    display: block;
    width: 34px; height: 34px;
    margin: 0 auto 14px;
    border-radius: 50%;
    background: var(--ink-light);
  }
  .card--front .brand { top: 118px; font-size: 28px; }
  .card--back .brand { top: 54px; font-size: 21px; }
  .card--back .brand__dot { width: 26px; height: 26px; margin-bottom: 10px; }

  .website {
    position: absolute;
    left: 0; right: 0;
    top: 300px;
    text-align: center;
    font-size: 15px;
    color: var(--ink-light);
    letter-spacing: 0.02em;
  }

  .name-bar {
    position: absolute;
    left: 250px;
    right: 0;
    top: 168px;
    height: 48px;
    background: linear-gradient(180deg, var(--bar-light) 0%, var(--bar-shade) 100%);
    display: flex;
    align-items: center;
    padding-left: 36px;
  }
  .name-bar__name {
    font-size: 30px;
    color: var(--bar-ink);
    letter-spacing: 0.01em;
  }

  .contacts {
    position: absolute;
    left: 300px;
    top: 232px;
    list-style: none;
    color: var(--ink-soft);
    font-size: 13px;
  }
  .contacts__item {
    display: flex;
    align-items: center;
    gap: 10px;
    height: 22px;
  }
  .contacts__icon {
    width: 14px; height: 14px;
    flex: none;
  }
</style>
</head>
<body>

  <section class="card card--front" aria-label="Card front">
    <div class="brand">
      <span class="brand__dot"></span>
      Velistra Design Collective
    </div>
    <p class="website">www.velistradesign.com</p>
  </section>

  <section class="card card--back" aria-label="Card back">
    <div class="brand">
      <span class="brand__dot"></span>
      Velistra Design Collective
    </div>

    <div class="name-bar">
      <span class="name-bar__name">Name Name</span>
    </div>

    <ul class="contacts">
      <li class="contacts__item">
        <svg class="contacts__icon" viewBox="0 0 14 14" aria-hidden="true">
          <path d="M7 1 L13 6.5 H11 V13 H8.5 V9 H5.5 V13 H3 V6.5 H1 Z" fill="var(--ink-light)"/>
        </svg>
        Street Number , Area , City
      </li>
      <li class="contacts__item">
        <svg class="contacts__icon" viewBox="0 0 14 14" aria-hidden="true">
          <circle cx="7" cy="7" r="7" fill="var(--ink-light)"/>
          <path d="M4.5 3.5 L6 3.5 L6.6 5.4 L5.7 6.1 Q6.6 7.9 7.9 8.3 L8.6 7.4 L10.5 8 L10.5 9.5 Q6 10 4.5 3.5 Z" fill="var(--card-mid)"/>
        </svg>
        0005550142870
      </li>
      <li class="contacts__item">
        <svg class="contacts__icon" viewBox="0 0 14 14" aria-hidden="true">
          <circle cx="7" cy="7" r="7" fill="var(--ink-light)"/>
          <rect x="3.5" y="4.5" width="7" height="5" fill="none" stroke="var(--card-mid)" stroke-width="1"/>
          <path d="M3.5 4.5 L7 7.5 L10.5 4.5" fill="none" stroke="var(--card-mid)" stroke-width="1"/>
        </svg>
        hello@velistradesign.com
      </li>
      <li class="contacts__item">
        <svg class="contacts__icon" viewBox="0 0 14 14" aria-hidden="true">
          <circle cx="7" cy="7" r="7" fill="var(--ink-light)"/>
          <circle cx="7" cy="7" r="3.6" fill="none" stroke="var(--card-mid)" stroke-width="1"/>
          <path d="M3.4 7 H10.6 M7 3.4 V10.6" stroke="var(--card-mid)" stroke-width="0.8"/>
        </svg>
        velistradesign.com
      </li>
    </ul>
  </section>

</body>
</html>
```